Fire Risk Assessment App needs a sleek UI design

I need a sleek, modern but professional design for my 5 page Fire Risk Assessment App. Include gradient background, fire themed colours including reds, yellows, light orange and a touch of black. Design must ooze simplicity and professionalism. This is for the UK market. See attached images and word doc for more information.

Target Market(s)

General public and business owners

Industry/Entity Type

Technology / Fire Safety

Colors
00AB8E
00BBA5
67D7C9
C6EFE9
E9F9F6
59FF00
82FF00
B8FF75
E3FFCB
F4FFEA
FFC000
F8CF3A
FAE287
FDF2CF
FEFAEE
F0912C
F2A743
F7CA91
FBE8D2
FDF5EE
EE7325
F08F49
F5BC92
FAE3D3
FDF4ED
EB3D1F
EC4F4E
F09395
F8D3D4
FCEDEE

```html
<!DOCTYPE html>
<html lang="en">
<head>
<meta charset="utf-8">
<title>Fire Risk Assessment App – UI Screens</title>
<link href="https://fonts.googleapis.com/css2?family=Lato:wght@400;700&display=swap" rel="stylesheet">
<style>
:root{
  --page:#ffffff;
  --grad-top:#F2A743;
  --grad-mid:#F08F49;
  --grad-low:#EE7325;
  --white:#ffffff;
  --cream:#FDF2CF;
  --soft-yellow:#FAE287;
  --gold:#FFC000;
  --green:#00AB8E;
  --grey-text:#7a7a7a;
  --active:#EB3D1F;
  --line:rgba(255,255,255,.45);
}
*{box-sizing:border-box;margin:0;padding:0}
html,body{width:1028px;height:1200px;overflow:hidden;background:var(--page)}
body{font-family:'Lato',sans-serif;position:relative}
.screen{position:absolute;top:275px;width:300px;height:650px;overflow:hidden;
  background:linear-gradient(170deg,var(--grad-mid) 0%,var(--grad-top) 30%,var(--grad-mid) 60%,var(--grad-low) 100%);color:var(--white)}
.screen--welcome{left:36px}
.screen--dashboard{left:364px}
.screen--support{left:692px}
.abs{position:absolute}
.center{left:0;right:0;text-align:center}
.title{font-size:23px;font-weight:700;line-height:1}
.subtitle{font-size:12px;line-height:1}
.tagline{font-size:17px;font-weight:700;line-height:1.3;color:var(--soft-yellow)}
.field{border:1px solid var(--line);border-radius:3px}
.btn{background:var(--white);color:var(--grey-text);font-size:13px;display:flex;align-items:center;justify-content:center;gap:8px;border-radius:2px}
.placeholder-doc{background:linear-gradient(160deg,#fdfaf4,#e9e4da);border-radius:3px;transform:rotate(-5deg);box-shadow:0 4px 10px rgba(0,0,0,.2)}
.round-icon{width:36px;height:36px;border-radius:50%;background:var(--white);display:flex;align-items:center;justify-content:center}
.plus{width:72px;height:72px;border-radius:50%;background:var(--white);display:flex;align-items:center;justify-content:center}
.photo-spot{width:76px;height:76px;border-radius:50%;border:2px solid var(--white)}
.photo-spot--commercial{background:linear-gradient(160deg,#8a97a8,#3c4656)}
.photo-spot--residential{background:linear-gradient(160deg,#c9b9a6,#5d7a4a)}
.label{font-size:13px;font-weight:700;color:var(--soft-yellow);text-align:center;width:100px}
.status-btn{width:130px;height:36px}
.item{font-size:13px;font-weight:700;color:var(--soft-yellow);display:flex;align-items:center;gap:9px;left:21px}
.dot{width:16px;height:16px;border-radius:50%;border:1.5px solid var(--white)}
.dot--filled{background:var(--white)}
.nav-line{left:12px;right:12px;top:594px;height:1px;background:var(--line)}
.nav-item{top:601px;width:42px;height:36px;border-radius:4px;display:flex;align-items:center;justify-content:center;transform:translateX(-50%)}
.nav-item--active{background:var(--active)}
.nav-item--active::after{content:"";position:absolute;bottom:-3px;left:6px;right:6px;height:2px;background:var(--white)}
.nav-dot{width:26px;height:26px;border-radius:50%;background:var(--white);display:flex;align-items:center;justify-content:center}
</style>
</head>
<body>

<!-- Welcome screen -->
<section class="screen screen--welcome">
  <h1 class="abs center title" style="top:14px">The Most 'User Friendly'</h1>
  <p class="abs center subtitle" style="top:44px">Fire Risk Assessment App available.</p>
  <div class="abs placeholder-doc" style="left:68px;top:76px;width:150px;height:190px" role="img" aria-label="Illustration of a printed fire risk assessment form"></div>
  <p class="abs center tagline" style="top:287px">Quick tap responses and voice<br>activated typing.</p>
  <div class="abs field" style="left:12px;top:344px;width:276px;height:36px">
    <svg class="abs" style="right:10px;top:8px" width="12" height="20" viewBox="0 0 12 20"><rect x="3" y="0" width="6" height="12" rx="3" fill="#fff"/><path d="M1 9a5 5 0 0 0 10 0M6 14v5M3 19h6" stroke="#fff" stroke-width="1.5" fill="none"/></svg>
  </div>
  <div class="abs btn" style="left:49px;top:391px;width:203px;height:36px">
    <svg width="22" height="20" viewBox="0 0 22 20"><circle cx="8" cy="5" r="4.5" fill="var(--gold)"/><path d="M0 19a8 7 0 0 1 16 0z" fill="var(--gold)"/><circle cx="17" cy="15" r="4.5" fill="var(--gold)" stroke="#fff"/><path d="M17 12.5v5M14.5 15h5" stroke="#fff" stroke-width="1.4"/></svg>
    Create a Free account</div>
  <p class="abs center tagline" style="top:442px">Any Responsible Person can do it.</p>
  <div class="abs btn" style="left:49px;top:472px;width:203px;height:36px">
    <svg width="22" height="20" viewBox="0 0 22 20"><circle cx="8" cy="5" r="4.5" fill="var(--gold)"/><path d="M0 19a8 7 0 0 1 16 0z" fill="var(--gold)"/><circle cx="17" cy="15" r="4.5" fill="var(--gold)" stroke="#fff"/><rect x="15" y="14.5" width="4" height="3" fill="#fff"/><path d="M15.8 14.5v-1a1.2 1.2 0 0 1 2.4 0v1" stroke="#fff" fill="none"/></svg>
    Customer Log in</div>
  <p class="abs center tagline" style="top:526px">Created and endorsed by British<br>Firefighters.</p>
  <svg class="abs" style="left:132px;top:578px" width="36" height="46" viewBox="0 0 36 46" fill="none" stroke="#fff" stroke-width="1.6" stroke-linecap="round">
    <path d="M6 12a15 15 0 0 1 24 0"/><path d="M3 24a15 15 0 0 1 30 0c0 6-1 12-4 17"/><path d="M8 40c-2-5-2-10-1-16a11 11 0 0 1 22 0c0 6 0 11-3 16"/><path d="M13 43c-2-6-2-12-1-19a6 6 0 0 1 12 0c0 7-1 13-3 19"/><path d="M18 24c0 8-1 14-2 20"/>
  </svg>
</section>

<!-- Dashboard screen -->
<section class="screen screen--dashboard">
  <div class="abs round-icon" style="left:20px;top:15px">
    <svg width="22" height="22" viewBox="0 0 22 22" fill="none" stroke="var(--active)" stroke-width="1.8" stroke-linecap="round"><path d="M4 16a8 8 0 1 1 14 0"/><path d="M11 13l4-6"/><circle cx="11" cy="13" r="1.5" fill="var(--active)"/></svg>
  </div>
  <h1 class="abs center title" style="top:21px">Dashboard</h1>
  <svg class="abs" style="left:0;top:0" width="300" height="200" viewBox="0 0 300 200" fill="none" stroke="#fff" stroke-width="1" stroke-dasharray="4 3"><path d="M120 100 Q85 110 83 147"/><path d="M180 100 Q215 110 216 147"/></svg>
  <div class="abs plus" style="left:113px;top:53px">
    <svg width="34" height="34" viewBox="0 0 34 34"><path d="M17 3v28M3 17h28" stroke="var(--gold)" stroke-width="7" stroke-linecap="round"/></svg>
  </div>
  <div class="abs photo-spot photo-spot--commercial" style="left:45px;top:147px" role="img" aria-label="Photo of commercial office towers"></div>
  <div class="abs photo-spot photo-spot--residential" style="left:178px;top:147px" role="img" aria-label="Photo of a residential house"></div>
  <p class="abs label" style="left:33px;top:227px">Commercial</p>
  <p class="abs label" style="left:166px;top:227px">Residential</p>

  <div class="abs btn status-btn" style="left:21px;top:259px">Complete
    <svg width="22" height="20" viewBox="0 0 22 20" fill="none" stroke="var(--green)" stroke-width="2"><circle cx="10" cy="11" r="8"/><path d="M6 11l4 4 10-13" stroke-width="2.6"/></svg></div>
  <div class="abs item" style="top:310px"><span class="dot dot--filled"></span>Milo's Barbershop</div>

  <div class="abs btn status-btn" style="left:21px;top:353px">In Progresso
    <svg width="20" height="20" viewBox="0 0 20 20"><circle cx="10" cy="10" r="7" fill="none" stroke="var(--green)" stroke-width="3.5"/></svg></div>
  <div class="abs item" style="top:406px"><span class="dot"></span>Heath Lane School</div>
  <div class="abs item" style="top:431px"><span class="dot"></span>Oak View Nursing Home</div>

  <div class="abs btn status-btn" style="left:21px;top:462px">Purchases
    <svg width="20" height="22" viewBox="0 0 20 22" fill="none" stroke="var(--green)" stroke-width="1.5"><path d="M2 7h12l1 13H1z"/><path d="M5 7V4a3 3 0 0 1 6 0v3"/><circle cx="15" cy="16" r="4.5" fill="#fff"/><path d="M13 16l1.5 1.5 3-3"/></svg></div>
  <div class="abs item" style="top:515px"><span class="dot"></span>Residential Fire Risk Assessment</div>
  <div class="abs item" style="top:540px"><span class="dot"></span>Ocommercial Fire Risk Assessment</div>
  <div class="abs item" style="top:563px"><span class="dot"></span>Commercial Fire Risk Assessment</div>

  <div class="abs nav-line"></div>
  <nav>
    <div class="abs nav-item nav-item--active" style="left:42px"><span class="nav-dot"><svg width="14" height="14" viewBox="0 0 22 22" fill="none" stroke="var(--active)" stroke-width="2.4"><path d="M4 16a8 8 0 1 1 14 0M11 13l4-6"/></svg></span></div>
    <div class="abs nav-item" style="left:115px"><span class="nav-dot"><svg width="14" height="12" viewBox="0 0 14 12" fill="none" stroke="var(--grad-low)" stroke-width="1.4"><rect x="1" y="2" width="12" height="9" rx="1"/><path d="M1 5h12"/></svg></span></div>
    <div class="abs nav-item" style="left:187px"><span class="nav-dot"><svg width="14" height="13" viewBox="0 0 14 13" fill="none" stroke="var(--grad-low)" stroke-width="1.4"><path d="M1 1h12v8H6l-3 3V9H1z"/></svg></span></div>
    <div class="abs nav-item" style="left:260px"><span class="nav-dot"><svg width="14" height="14" viewBox="0 0 14 14" fill="none" stroke="var(--grad-low)" stroke-width="1.4"><circle cx="7" cy="7" r="5.5"/><path d="M4 10l6-6"/></svg></span></div>
  </nav>
</section>

<!-- Technical support screen -->
<section class="screen screen--support">
  <div class="abs round-icon" style="left:13px;top:14px">
    <svg width="20" height="18" viewBox="0 0 14 13" fill="none" stroke="var(--active)" stroke-width="1.2"><path d="M1 1h12v8H6l-3 3V9H1z"/><circle cx="4.5" cy="5" r=".6" fill="var(--active)"/><circle cx="7" cy="5" r=".6" fill="var(--active)"/><circle cx="9.5" cy="5" r=".6" fill="var(--active)"/></svg>
  </div>
  <h1 class="abs title" style="left:0;width:300px;padding-left:0;text-align:center;top:16px">Technical Support</h1>
  <p class="abs center subtitle" style="top:45px">Type/record Your Response Here.</p>
  <svg class="abs" style="left:272px;top:40px" width="12" height="20" viewBox="0 0 12 20"><rect x="3" y="0" width="6" height="12" rx="3" fill="#fff"/><path d="M1 9a5 5 0 0 0 10 0M6 14v5M3 19h6" stroke="#fff" stroke-width="1.5" fill="none"/></svg>
  <div class="abs field" style="left:12px;top:71px;width:276px;height:101px"></div>
  <div class="abs btn" style="left:216px;top:185px;width:73px;height:36px">Send</div>

  <div class="abs nav-line"></div>
  <nav>
    <div class="abs nav-item" style="left:41px"><span class="nav-dot"><svg width="14" height="14" viewBox="0 0 22 22" fill="none" stroke="var(--grad-low)" stroke-width="2.4"><path d="M4 16a8 8 0 1 1 14 0M11 13l4-6"/></svg></span></div>
    <div class="abs nav-item" style="left:114px"><span class="nav-dot"><svg width="14" height="12" viewBox="0 0 14 12" fill="none" stroke="var(--grad-low)" stroke-width="1.4"><rect x="1" y="2" width="12" height="9" rx="1"/><path d="M1 5h12"/></svg></span></div>
    <div class="abs nav-item nav-item--active" style="left:186px"><span class="nav-dot"><svg width="14" height="13" viewBox="0 0 14 13" fill="none" stroke="var(--active)" stroke-width="1.4"><path d="M1 1h12v8H6l-3 3V9H1z"/></svg></span></div>
    <div class="abs nav-item" style="left:259px"><span class="nav-dot"><svg width="14" height="14" viewBox="0 0 14 14" fill="none" stroke="var(--grad-low)" stroke-width="1.4"><circle cx="7" cy="7" r="5.5"/><path d="M4 10l6-6"/></svg></span></div>
  </nav>
</section>

</body>
</html>
```